Glofarvik - Start-up company selling electricity

Hello let me tell you about Glofarvik.

Glofarvik is start-up company selling electricity in Iceland. The operations of the company consist of making power usage forecasts for our customers, purchasing the electricity wholesale from the energy producers, and selling the electricity to the consumer. We are focused on tech by using optimization and machine learning to minimize electricity prices to our customers. Our marketing strategy is to portray a tech company mindset and to show dedication to driving down the electricity price on the market.

We need your help to make our website pop. Possible concepts to work with are as follows:

- Iceland the land of ice and fire
- Green energy
- Innovation
- Tech and data science

Link to our website: https://prufa.glofarvik-example.is/
We are open to ideas.
Thank you!

Target Market(s)

Electricity consumers both homes and companies.

Number of Pages Required

1 page

Font styles to use
Serif
Sans Serif

```html
<!DOCTYPE html>
<html lang="en">
<head>
<meta charset="utf-8">
<title>Glofarvik – Green Energy</title>
<link rel="stylesheet" href="https://fonts.googleapis.com/css2?family=Libre+Baskerville:wght@700&family=Poppins:wght@400;500;600;700&display=swap">
<style>
:root{
  --teal:#0b6459;
  --ink:#111111;
  --text:#333333;
  --muted:#555555;
  --panel:#f4f4f4;
  --white:#ffffff;
  --footer:#000000;
  --line:#2a2a2a;
}
*{box-sizing:border-box;margin:0;padding:0}
html,body{width:1200px;height:2400px;overflow:hidden;background:var(--white)}
body{font-family:"Poppins",sans-serif;color:var(--text);position:relative}
a{color:inherit;text-decoration:none}

.site-nav{height:96px;display:flex;align-items:center;padding:0 128px 0 152px;justify-content:space-between}
.brand{display:flex;align-items:center;gap:8px;font-family:"Libre Baskerville",serif;font-weight:700;font-size:15px;color:var(--teal)}
.brand-dot{width:20px;height:20px;border-radius:50%;background:var(--teal)}
.nav-links{display:flex;gap:32px;font-size:13px;color:var(--ink)}

.hero{height:590px;position:relative;text-align:center}
.hero-title{font-family:"Libre Baskerville",serif;font-weight:700;font-size:72px;letter-spacing:1px;color:var(--teal);padding-top:90px;line-height:1}
.hero-sub{font-family:"Poppins",sans-serif;font-weight:600;font-size:42px;color:var(--ink);margin-top:12px;letter-spacing:1px}
.hero-art{position:absolute;left:150px;right:110px;top:320px;height:250px;border-radius:4px;
  background:linear-gradient(180deg,#ffffff 0%,#e6e9ec 45%,#c9cfd4 70%,#4caf50 86%,#2f7d3a 100%)}

.tagline{text-align:center;font-weight:600;font-size:41px;color:var(--ink);margin-top:8px}
.tagline em{font-style:normal;color:var(--teal)}

.cards{display:flex;gap:22px;padding:0 28px;margin-top:50px}
.card{flex:1;height:282px;border:1.5px solid var(--teal);padding:28px 32px}
.card-head{display:flex;align-items:center;gap:12px;font-size:18px;font-weight:500;color:var(--ink)}
.card-head span{color:var(--teal)}
.card-actions{display:flex;flex-direction:column;align-items:center;gap:24px;margin-top:36px}
.btn{width:222px;height:48px;display:flex;align-items:center;justify-content:center;color:var(--white);font-size:15px}
.btn-dark{background:var(--ink)}
.btn-teal{background:var(--teal)}
.price{text-align:center;margin-top:14px}
.price-value{font-size:29px;color:var(--teal);line-height:1.1}
.price-unit{font-size:10px;color:var(--muted);margin-bottom:10px}
.price-note{text-align:center;font-size:13px;color:var(--muted);line-height:1.8;margin-top:16px}
.card-copy{font-size:13.5px;line-height:1.45;color:var(--muted);margin-top:40px;padding:0 12px}

.feature{display:flex;height:320px}
.feature + .feature{margin-top:44px}
.feature-first{margin-top:92px}
.feature-media{width:542px;height:100%}
.feature-body{flex:1;padding:48px 110px 0 110px}
.feature-panel{background:var(--panel)}
.feature-reverse .feature-body{padding:50px 60px 0 102px}
.feature-title{font-weight:600;font-size:34px;color:var(--teal);letter-spacing:.5px;line-height:1.2}
.feature-title .dark{color:var(--ink)}
.feature-copy{font-size:10px;line-height:2.4;color:var(--text);margin-top:14px;max-width:440px}
.btn-outline{display:inline-flex;align-items:center;justify-content:center;width:158px;height:42px;border:2px solid var(--teal);color:var(--ink);font-weight:600;font-size:15px;margin-top:20px}

.media-solar{background:linear-gradient(180deg,#2f6fc0 0%,#f5c260 38%,#6a8bb8 58%,#4e6a3a 100%)}
.media-lava{background:radial-gradient(ellipse at 30% 60%,#f26b1d 0%,#5a2a1a 22%,#cfd6dd 45%,#e9edf1 100%)}
.media-data{background:radial-gradient(ellipse at 50% 50%,#1fb6ff 0%,#0a52c8 45%,#04164d 100%)}

.site-footer{position:absolute;left:0;top:2200px;width:1200px;height:200px;background:var(--footer);color:var(--white)}
.footer-grid{display:flex;padding:36px 0 0 100px;height:170px}
.footer-brand{width:308px}
.footer-logo{display:flex;align-items:center;gap:10px;font-family:"Libre Baskerville",serif;font-weight:700;font-size:28px}
.footer-logo i{width:26px;height:26px;border-radius:50%;background:var(--white)}
.footer-about{font-size:8px;line-height:1.5;margin-top:12px;padding-left:8px;width:230px}
.footer-col{font-size:9px;line-height:1.9}
.footer-col h4{font-weight:400;font-size:9px;margin-bottom:14px;letter-spacing:.3px}
.col-links{width:180px}
.col-address{width:186px}
.col-contact{width:245px}
.icon-row{display:flex;align-items:flex-start;gap:8px}
.socials{display:flex;gap:8px;margin-top:2px}
.socials i{width:14px;height:14px;border-radius:50%;background:var(--white)}
.copyright{border-top:1px solid var(--line);height:30px;display:flex;align-items:center;justify-content:center;font-size:10px;letter-spacing:1px}
</style>
</head>
<body>
<header class="site-nav">
  <a class="brand" href="https://prufa.glofarvik-example.is/"><i class="brand-dot"></i>GLOFARVIK</a>
  <nav class="nav-links">
    <a href="#">TERMS OF BUSINESS</a>
    <a href="#">QUESTION &amp; ANSWER</a>
    <a href="#">ABOUT</a>
    <a href="#">GLOFARVIK</a>
  </nav>
</header>

<section class="hero">
  <h1 class="hero-title">GLOFARVIK</h1>
  <p class="hero-sub">GREEN ENERGY</p>
  <div class="hero-art" role="img" aria-label="Illustration of a green landscape with a city skyline, wind turbines, trees and solar panels"></div>
</section>

<h2 class="tagline">Same Electricity ~ <em>Just Cheaper!</em></h2>

<section class="cards">
  <article class="card">
    <div class="card-head">
      <svg width="40" height="50" viewBox="0 0 40 50" fill="none" stroke="#0b6459" stroke-width="2"><path d="M12 2v10M28 2v10M6 12h28v14a14 14 0 0 1-28 0z"/><path d="M22 17l-6 9h7l-4 8"/><path d="M20 40v8"/></svg>
      <div>Welcome <span>To</span> Business</div>
    </div>
    <div class="card-actions">
      <a class="btn btn-dark" href="#">Company</a>
      <a class="btn btn-teal" href="#">Home</a>
    </div>
  </article>
  <article class="card">
    <div class="card-head" style="padding-left:22px">
      <svg width="52" height="40" viewBox="0 0 52 40" fill="none" stroke="#0b6459" stroke-width="2"><ellipse cx="26" cy="22" rx="20" ry="14"/><circle cx="24" cy="20" r="8"/><path d="M24 15v10M21 18h5M22 23h5"/><path d="M46 20h4v6h-4"/></svg>
      <div style="margin-left:18px">Price <span>List</span></div>
    </div>
    <div class="price">
      <div class="price-value">6.95</div><div class="price-unit">ISK / KWh</div>
      <div class="price-value">6.22</div><div class="price-unit">ISK / KWh</div>
    </div>
    <p class="price-note">electric acceleration<br>make a price comparison</p>
  </article>
  <article class="card">
    <div class="card-head">
      <svg width="32" height="40" viewBox="0 0 32 40" fill="none" stroke="#0b6459" stroke-width="2"><path d="M20 2L4 22h12l-6 16 20-22H18z"/></svg>
      <div>The Future <span>Is</span> Exciting</div>
    </div>
    <p class="card-copy">Let's make the electricity system smarter together. Glofarvik uses artificial intelligence, data science and automation to minimize costs and promote eccentricity</p>
  </article>
</section>

<section class="feature feature-first feature-panel">
  <div class="feature-media media-solar" role="img" aria-label="Photo of solar panels in a field at sunset with a city skyline"></div>
  <div class="feature-body">
    <h3 class="feature-title">INNOVATION</h3>
    <p class="feature-copy">Lorem Ipsum is simply dummy text of the printing and typesetting industry. Lorem Ipsum has been the industry's standard dummy text ever since the 1500s, when an unknown printer took a galley of type and scrambled it to make a type specimen book. It has survived not only five centuries, but also the leap into electronic typesetting, remaining essentially unchanged.</p>
    <a class="btn-outline" href="#">READ MORE</a>
  </div>
</section>

<section class="feature feature-reverse">
  <div class="feature-body">
    <h3 class="feature-title"><span class="dark">THE LAND OF</span> ICE AND FIRE</h3>
    <p class="feature-copy">Lorem Ipsum is simply dummy text of the printing and typesetting industry. Lorem Ipsum has been the industry's standard dummy text ever since the 1500s, when an unknown printer took a galley of type and scrambled it to make a type specimen book. It has survived not only five centuries, but also the leap into electronic typesetting, remaining essentially unchanged.</p>
    <a class="btn-outline" href="#">READ MORE</a>
  </div>
  <div class="feature-media media-lava" role="img" aria-label="Photo of glowing lava flowing across snow"></div>
</section>

<section class="feature feature-panel">
  <div class="feature-media media-data" role="img" aria-label="Blue digital data interface background"></div>
  <div class="feature-body" style="padding-left:100px">
    <h3 class="feature-title">TECH <span class="dark">AND</span> DATA SCIENCE</h3>
    <p class="feature-copy">Lorem Ipsum is simply dummy text of the printing and typesetting industry. Lorem Ipsum has been the industry's standard dummy text ever since the 1500s, when an unknown printer took a galley of type and scrambled it to make a type specimen book. It has survived not only five centuries, but also the leap into electronic typesetting, remaining essentially unchanged.</p>
    <a class="btn-outline" href="#">READ MORE</a>
  </div>
</section>

<footer class="site-footer">
  <div class="footer-grid">
    <div class="footer-brand">
      <div class="footer-logo"><i></i>GLOFARVIK</div>
      <p class="footer-about">The operations of the company consist of making power usage forecasts for our customers, purchasing the electricity wholesale from the energy producers, and selling the electricity to the consumer.</p>
    </div>
    <div class="footer-col col-links">
      <h4>QUICK LINKS</h4>
      <a href="#">terms of business</a><br><a href="#">question and answer</a><br><a href="#">about glofarvik</a>
    </div>
    <div class="footer-col col-address">
      <h4>ADDRESS</h4>
      <div class="icon-row">
        <svg width="12" height="14" viewBox="0 0 12 14" fill="none" stroke="#fff" stroke-width="1.2"><path d="M6 13s5-5 5-8A5 5 0 0 0 1 5c0 3 5 8 5 8z"/><circle cx="6" cy="5" r="1.8"/></svg>
        <div>HAFNARBRAUT 8<br>200 KOPAVOGUR</div>
      </div>
    </div>
    <div class="footer-col col-contact">
      <h4>CONTACT US</h4>
      <div class="icon-row"><svg width="13" height="10" viewBox="0 0 13 10" fill="none" stroke="#fff" stroke-width="1"><rect x=".5" y=".5" width="12" height="9"/><path d="M.5.5l6 5 6-5"/></svg>hallo@glofarvik-example.is</div>
      <div class="icon-row"><svg width="12" height="12" viewBox="0 0 12 12" fill="#fff"><path d="M2 1l2 0 1 3-1.5 1a7 7 0 0 0 3.5 3.5L8 7l3 1v2a1 1 0 0 1-1 1A9 9 0 0 1 1 2a1 1 0 0 1 1-1z"/></svg>555-0199</div>
    </div>
    <div class="footer-col">
      <h4>FOLLOW US</h4>
      <div class="socials"><i></i><i></i><i></i><i></i></div>
    </div>
  </div>
  <div class="copyright">copyright © glofarvik 2021 all rights reserved</div>
</footer>
</body>
</html>
```